Journal Cover Design Project

The Worldwide Review of Rising Trade Systems is a professional journal which aims to provide an international platform for publication of original research on the emerging economies.
The journal is published three times a year and available by subscription. Currently, the cover design is the same for each issue. We are looking to redesign the cover (and interior) of our journal and would like a design that would allow us to change the color scheme for each issue or volume while maintaining a consistent design scheme.
Our design preference is simple and modern with good use of color. Many of our past publications have used abstract maps/globes but we are open to new ideas. We would need a creative way to include text on the cover, possibly a way to present the article titles or main topics for each issue. For example, we like the use of color and the general design in this image: http://www.pixmoravo.example/photos/drawdreamhope/5182640913/lightbox/
Below is a link to our most recent issue of the journal. You can see an example of the article titles, structure, etc. The website also shows the current cover of the journal (but we do not want the new design to be based off of the current one):
http://rts.quilberpress.example/content/4/2.toc

```html
<!DOCTYPE html>
<html lang="en">
<head>
<meta charset="utf-8">
<title>Worldwide Review of Rising Trade Systems — Volume 5 Issue 1</title>
<link rel="stylesheet" href="https://fonts.googleapis.com/css2?family=Roboto+Condensed:wght@400;700&display=swap">
<style>
  :root {
    --coral: #ef5458;
    --coral-light: #f57a7c;
    --lime: #9ccc3c;
    --ink: #1b1b1b;
    --paper: #ffffff;
    --stone-light: #eeeeee;
    --stone-dark: #9a9a9a;
    --backdrop: #ffffff;
  }
  * { margin: 0; padding: 0; box-sizing: border-box; }
  html, body {
    width: 1001px; height: 1200px; overflow: hidden;
    background: var(--backdrop);
    font-family: "Roboto Condensed", "Arial Narrow", sans-serif;
    color: var(--ink);
  }
  .cover {
    position: absolute; left: 69px; top: 36px;
    width: 862px; height: 1110px;
    background: var(--paper);
    overflow: hidden;
    box-shadow: 4px 6px 14px rgba(0,0,0,0.35);
  }
  .tower-photo {
    position: absolute; left: 0; top: 120px; width: 862px; height: 965px;
    background: linear-gradient(100deg, #ffffff 0%, #f3f3f3 30%, #c9c9c9 55%, #e6e6e6 70%, #a9a9a9 100%);
  }
  .graphics { position: absolute; inset: 0; }
  .date {
    position: absolute; right: 40px; top: 166px;
    color: var(--paper); font-weight: 700; font-size: 31px; letter-spacing: 0.5px;
  }
  .globe {
    position: absolute; left: 40px; top: 204px; width: 240px; height: 240px;
    border-radius: 50%;
    background: radial-gradient(circle at 38% 35%, #ffffff 0%, #e2e2e2 55%, #a8a8a8 100%);
    opacity: 0.85;
  }
  .masthead { position: absolute; left: 64px; top: 268px; }
  .masthead-main {
    color: var(--lime); font-weight: 700; font-size: 84px; line-height: 1; letter-spacing: -0.5px;
  }
  .masthead-sub {
    font-weight: 700; font-size: 44px; line-height: 1; margin-top: 8px; margin-left: 2px;
  }
  .headline { position: absolute; left: 64px; }
  .headline span {
    display: inline-block; background: var(--paper); padding: 0 6px;
  }
  .headline-title { font-weight: 700; font-size: 37px; line-height: 40px; }
  .headline-deck  { font-weight: 700; font-size: 19px; line-height: 22px; }
  .issue-mark { position: absolute; left: 664px; top: 846px; width: 140px; height: 150px; }
  .issue-volume {
    position: absolute; left: 0; top: 0;
    writing-mode: vertical-rl; transform: rotate(180deg);
    font-weight: 700; font-size: 30px; line-height: 30px; letter-spacing: 1px;
  }
  .issue-number {
    position: absolute; left: 36px; top: -20px;
    font-weight: 700; font-size: 132px; line-height: 1;
  }
  .issue-label {
    position: absolute; left: 0; top: 104px;
    font-weight: 700; font-size: 29px; letter-spacing: 0.5px;
  }
  .publisher-strip {
    position: absolute; left: 622px; top: 996px; width: 176px; height: 56px;
    background: var(--paper);
    display: flex; align-items: center; gap: 8px; padding: 0 8px;
  }
  .publisher-dot { width: 20px; height: 20px; border-radius: 50%; background: var(--ink); flex: none; }
  .publisher-name { font-weight: 700; font-size: 13px; line-height: 14px; }
  .footer-band {
    position: absolute; left: 0; top: 1085px; width: 862px; height: 13px;
    background: var(--lime);
  }
</style>
</head>
<body>
  <div class="cover">
    <div class="tower-photo" role="img" aria-label="Black and white photograph of a tall office tower seen from below"></div>

    <svg class="graphics" width="862" height="1110" viewBox="0 0 862 1110">
      <defs>
        <linearGradient id="coral-wash" x1="0" y1="0" x2="1" y2="1">
          <stop offset="0" stop-color="var(--coral)"/>
          <stop offset="0.6" stop-color="var(--coral-light)"/>
          <stop offset="1" stop-color="var(--coral)"/>
        </linearGradient>
      </defs>
      <polygon points="0,0 862,0 862,150 420,181 0,120" fill="url(#coral-wash)" role="img" aria-label="Coral band with a fine curved line pattern"/>
      <polygon points="420,181 862,150 862,245" fill="var(--lime)"/>
      <line x1="0" y1="120" x2="862" y2="245" stroke="var(--ink)" stroke-width="6"/>
      <polygon points="446,459 862,462 862,536" fill="var(--lime)"/>
      <line x1="0" y1="456" x2="862" y2="462" stroke="var(--ink)" stroke-width="6"/>
    </svg>

    <div class="date">08/2012</div>
    <div class="globe" role="img" aria-label="Silver wireframe globe"></div>

    <div class="masthead">
      <div class="masthead-main">Worldwide Review</div>
      <div class="masthead-sub">of Rising Trade Systems</div>
    </div>

    <div class="headline" style="top:580px">
      <div class="headline-title"><span>Construction and Analysis</span></div>
      <div class="headline-deck"><span>of a Global GDP Growth Model for<br>185 Countries through 2050</span></div>
    </div>
    <div class="headline" style="top:700px">
      <div class="headline-title"><span>A New Vision<br>for Mexico 2042</span></div>
      <div class="headline-deck"><span>Achieving Prosperity for All</span></div>
    </div>
    <div class="headline" style="top:848px">
      <div class="headline-title"><span>India 2039</span></div>
      <div class="headline-deck"><span>Transforming Agriculture:<br>Productivity, Markets,<br>and Institutions</span></div>
    </div>
    <div class="headline" style="top:998px">
      <div class="headline-title"><span>New Directions</span></div>
      <div class="headline-deck"><span>for Water Management in Indian Agriculture</span></div>
    </div>

    <div class="issue-mark">
      <div class="issue-volume">VOLUME</div>
      <div class="issue-number">5</div>
      <div class="issue-label">ISSUE 1</div>
    </div>

    <div class="publisher-strip">
      <span class="publisher-dot"></span>
      <span class="publisher-name">Rising Markets Circle<br>Quilber Press</span>
    </div>

    <div class="footer-band"></div>
  </div>
</body>
</html>
```